Cover design for series of 4 Best Practice Guides

The Design Brief
We are looking for cover designs for a series of 4 industry Best Practice Guides (BPG):

1. Best Practice Guide: Repossessions
2. Best Practice Guide: Collections
3. Best Practice Guide: Investigations
4. Best Practice Guide: Process Serving

The only essential elements to be included in the design are:
1. our logo (attached in both blue and white - either is acceptable)
2. Publication Name

We are looking for a set of 4 clean and professional looking designs which are clearly linked/related but where each BPG is distinguishable as a different publication either by the use of colour or by the use of appropriate imagery (illustrations, appropriate photos etc).

The BPGs will be produced in both A4 hard copy and electronic format.

Files should be provided in either AI or PSD format.

Some Background Information
These BPGs are being produced by the Guild of Ledgerwick Brokers ([login to view URL]) an industry association in Australia representing collectors, investigators, process servers and repossession agents. Broadly known as mercantile agents, below is a brief description of each role:

o Collectors make demands for payment of overdue debts (often pursuant to a formal contract) and enter into dialogue with individual and corporate debtors in order to achieve resolution of delinquent accounts whether by full or part recovery or by establishing the debtor does not have the means to pay.

o Investigators inquire into, and obtain information about, the personal character or actions of persons, together with the character or nature of the business or occupation of any person.

o Process servers deliver court issued process for a variety of reasons including debt recovery, family law proceedings, civil and criminal litigation in strict accordance with the rules of the issuing court.

o Repossession agents act for principals to formal contracts (leases, bills of sale, hire purchase agreements etc.) to either seek payment of arrears or the balance of the loan facility or else to recover the security for the facility (cars, motor cycles etc.).

Below is an extract from the Repossession BPG:

INTRODUCTION: BEST PRACTICE GUIDE
The Guild of Ledgerwick Brokers is the industry association nationally representing businesses and persons engaged in collections, investigations, process serving and repossession services in Australia.
Membership of the GLB is voluntary - businesses and persons join to demonstrate their commitment to the high standards adopted and promoted by the association.

This Best Practice Guide sets out best practice standards expected from members involved in the provision of repossession services and which debtors and businesses engaging with members should expect. Members agree to comply with this Best Practice Guide by virtue of membership.

We believe that this Best Practice Guide will enable debtors and businesses to address their situation involving the repossession of goods in confidence of fair treatment by members. To fulfil the potential of this Best Practice Guide those with debts outstanding for which repossession of goods is involved must cooperate with the businesses managing their debts including the repossession of security items so as to agree to reasonable solutions.

This Best Practice Guide is intended as a helpful resource for debtors and creditors, whilst compliance by members is intended to ensure best practice standards are maintained.

```html
<!DOCTYPE html>
<html lang="en">
<head>
<meta charset="utf-8">
<title>Best Practise Guide: Collection</title>
<link rel="stylesheet" href="https://fonts.googleapis.com/css2?family=Arimo:wght@400;700&display=swap">
<style>
  :root {
    --cover-yellow: #fef01c;
    --ink-charcoal: #383838;
  }
  html, body {
    margin: 0;
    padding: 0;
    overflow: hidden;
    background: var(--cover-yellow);
  }
  .guide-cover {
    position: relative;
    width: 1023px;
    height: 1200px;
    background: var(--cover-yellow);
    overflow: hidden;
  }
  .guide-cover__art {
    position: absolute;
    inset: 0;
    width: 1023px;
    height: 1200px;
    display: block;
  }
  .guide-title {
    font-family: "Arimo", Arial, sans-serif;
    font-weight: 700;
    font-size: 101px;
    fill: var(--ink-charcoal);
  }
  .dollar-mark {
    font-family: "Arimo", Arial, sans-serif;
    font-weight: 400;
    font-size: 300px;
    fill: var(--cover-yellow);
  }
  .guide-series {
    font-family: "Arimo", Arial, sans-serif;
    font-weight: 400;
    font-size: 66px;
    fill: var(--ink-charcoal);
  }
  .publisher-name {
    font-family: "Arimo", Arial, sans-serif;
    font-weight: 700;
    font-size: 62px;
    fill: var(--ink-charcoal);
  }
</style>
</head>
<body>
  <main class="guide-cover">
    <svg class="guide-cover__art" viewBox="0 0 1023 1200" xmlns="http://www.w3.org/2000/svg">
      <text class="guide-title" x="523" y="356" text-anchor="middle"
            textLength="740" lengthAdjust="spacingAndGlyphs"
            transform="rotate(-11.5 523 321)">COLLECTION</text>

      <polygon class="emblem-triangle" points="527,357 297,732 759,732" fill="var(--ink-charcoal)"/>
      <text class="dollar-mark" x="541" y="690" text-anchor="middle">$</text>

      <text class="guide-series" x="233" y="812"
            textLength="653" lengthAdjust="spacingAndGlyphs">Best Practise Guide</text>

      <text class="publisher-name" x="984" y="1010" text-anchor="end">GLB</text>
    </svg>
  </main>
</body>
</html>
```